Re-design association of teachers webplattform

I need a complete re-design for an existing association of teachers website. I will create it in wordpress in the next months.

It should be modern, but more an information plattform for teachers in our region (Switzerland, south -> near the alps).
Following content are contained:
- blog
- calendar
- text only
- document only (a list of documents to download -> pdf)
- social media
- login area

What I need is :
- a well color concept
- an inspiration how to use images (or without images)
- an inspiration where to place logo (attached file) / text / navigation

```html
<!DOCTYPE html>
<html lang="en">
<head>
<meta charset="utf-8">
<title>ALPEDU – Association of teachers</title>
<link href="https://fonts.googleapis.com/css2?family=Rubik:wght@500;600;700&family=Roboto:wght@400;500;700&display=swap" rel="stylesheet">
<style>
:root{
  --green:#7aa51b;
  --green-light:#c8da6c;
  --blue:#0b8fce;
  --ink:#111111;
  --text:#555555;
  --grey-bg:#f2f2f2;
  --line:#dddddd;
  --white:#ffffff;
  --black:#000000;
}
*{box-sizing:border-box;margin:0;padding:0}
html,body{width:1200px;height:3253px;overflow:hidden}
body{position:relative;background:var(--white);font-family:"Roboto",sans-serif;color:var(--ink)}
.abs{position:absolute}
.heading{font-family:"Rubik",sans-serif;font-weight:600;color:var(--ink);text-transform:uppercase}
.btn{position:absolute;display:flex;align-items:center;justify-content:center;border-radius:30px;color:var(--white);font-family:"Roboto",sans-serif;font-weight:700;font-size:14px;text-transform:uppercase;letter-spacing:-.2px}
.btn-green{background:var(--green)}
.btn-blue{background:var(--blue)}

/* header */
.top-line{top:0;left:0;width:1200px;height:5px;background:var(--green-light)}
.site-header{top:5px;left:0;width:1200px;height:97px;background:var(--white)}
.brand{left:111px;top:30px;display:flex;align-items:center;gap:8px;font-family:"Rubik",sans-serif;font-weight:700;font-size:28px;color:var(--blue)}
.brand-dot{width:18px;height:18px;border-radius:50%;background:var(--green)}
.main-nav{left:273px;top:46px;display:flex;gap:24px;font-size:13.5px;font-weight:700;color:var(--ink)}
.main-nav .active{color:var(--green);border-bottom:2px solid var(--green);padding-bottom:6px}
.nav-search{width:13px;height:13px}

/* hero */
.hero{top:102px;left:0;width:1200px;height:640px;overflow:hidden}
.hero-photo{position:absolute;inset:0;background:linear-gradient(180deg,#cfd8dc 0%,#b9b3a8 45%,#8b7d6f 100%)}
.hero-title{position:absolute;top:108px;width:1200px;text-align:center;font-family:"Rubik",sans-serif;font-weight:700;font-size:48px;color:var(--ink)}
.hero-sub{position:absolute;top:174px;width:1200px;text-align:center;font-size:21px;color:var(--ink)}
.hero-dots{position:absolute;top:561px;left:561px;display:flex;gap:7px}
.hero-dots span{width:13px;height:13px;border-radius:50%;border:2px solid var(--green)}
.hero-dots .on{background:var(--green);box-shadow:inset 0 0 0 2px var(--white)}
.hero-curve{position:absolute;left:0;bottom:0}

/* intro */
.intro-frame{left:111px;top:822px;width:488px;height:386px;border:6px solid var(--green);border-radius:4px}
.intro-photo{left:129px;top:840px;width:487px;height:384px;border-radius:4px;background:linear-gradient(160deg,#e8eaec 0%,#b8c0c8 50%,#4a4f57 100%)}
.intro-title{left:684px;top:858px;font-size:24px}
.bullet-list{left:684px;top:916px;width:410px;list-style:none}
.bullet-list li{position:relative;padding-left:41px;font-size:14px;line-height:24px;color:var(--text);margin-bottom:11px}
.bullet-list li svg{position:absolute;left:0;top:5px}

/* protect */
.protect{top:1314px;left:0;width:1200px;height:440px;background:var(--grey-bg)}
.protect-title{top:1379px;width:1200px;text-align:center;font-size:29px}
.card{position:absolute;top:1456px;width:231px;height:205px;background:var(--white);border-radius:4px;box-shadow:0 2px 8px rgba(0,0,0,.06);text-align:center}
.card-icon{width:64px;height:64px;margin:36px auto 20px;border-radius:8px;background:#e6eecf}
.card-text{font-family:"Rubik",sans-serif;font-weight:500;font-size:17px;line-height:26px;color:var(--blue);text-transform:uppercase}

/* blog */
.blog-bg{left:0;top:1720px}
.blog-title{top:1806px;width:1200px;text-align:center;font-size:36px;font-weight:700}
.post{position:absolute;top:1894px;width:476px;height:267px;background:var(--white);border-radius:4px;padding:26px 26px}
.post-title{font-family:"Rubik",sans-serif;font-weight:500;font-size:18px;color:var(--ink)}
.post-date{display:flex;align-items:center;gap:8px;margin-top:14px;font-size:13.5px;font-weight:500;color:#444}
.post-text{margin-top:16px;font-size:13.5px;line-height:23px;color:var(--text)}
.post .btn{left:27px;bottom:29px;width:118px;height:50px}
.follow{position:absolute;right:33px;bottom:29px;width:186px;height:50px;border-radius:25px;background:#f2f2f2;display:flex;align-items:center;padding-left:22px;gap:8px;font-size:13.5px;color:#555}
.follow i{width:10px;height:10px;border-radius:50%;background:var(--green);display:block}
.follow i+i{background:var(--blue)}
.follow i+i+i{background:#777}

/* contact */
.contact-title{top:2374px;width:1200px;text-align:center;font-size:36px;font-weight:700}
.field{position:absolute;border:2px solid #e4e4e4;border-radius:2px;font-size:15px;color:#999;padding:0 16px;display:flex;align-items:center;box-shadow:0 1px 3px rgba(0,0,0,.04)}
.field.area{align-items:flex-start;padding-top:16px}

/* footer */
.footer-curve{left:0;top:2835px}
.footer{top:2968px;left:0;width:1200px;height:285px;background:var(--black);color:var(--white)}
.foot-head{position:absolute;top:25px;font-family:"Rubik",sans-serif;font-weight:600;font-size:18px;text-transform:uppercase}
.newsletter{position:absolute;left:111px;top:69px;width:327px;height:46px;background:var(--white);border-radius:3px;display:flex;align-items:center;justify-content:space-between;padding:0 4px 0 16px;color:#777;font-size:13px}
.newsletter span.join{background:var(--green);color:var(--white);font-size:12.5px;padding:11px 14px;border-radius:2px}
.socials{position:absolute;left:111px;top:142px;display:flex;gap:8px}
.socials i{width:34px;height:34px;border-radius:50%;border:2px solid var(--green);display:block}
.socials i:first-child{background:var(--green)}
.foot-list{position:absolute;list-style:none;font-size:14px;line-height:20px}
.foot-list li{position:relative;padding-left:35px;margin-bottom:9px}
.foot-list li svg{position:absolute;left:0;top:3px}
.foot-brand{position:absolute;left:943px;top:40px;display:flex;align-items:center;gap:10px;font-family:"Rubik",sans-serif;font-weight:700;font-size:36px;color:var(--white)}
.foot-brand i{width:22px;height:22px;border-radius:50%;background:var(--white);display:block}
.foot-rule{position:absolute;left:111px;top:226px;width:977px;height:1px;background:#333}
.copyright{position:absolute;top:243px;width:1200px;text-align:center;font-size:13.5px}
</style>
</head>
<body>

<div class="abs top-line"></div>
<header class="abs site-header"></header>
<div class="abs brand"><span>ALPEDU</span><span class="brand-dot"></span></div>
<nav class="abs main-nav">
  <span class="active">HOME</span><span>STATUTES AND PROTOCOLS</span><span>BOARD</span><span>DELEGATES</span><span>CONTACT &nbsp;|</span>
  <svg class="nav-search" viewBox="0 0 14 14"><circle cx="6" cy="6" r="4.5" fill="none" stroke="#111" stroke-width="2"/><line x1="9.5" y1="9.5" x2="13" y2="13" stroke="#111" stroke-width="2"/></svg>
</nav>
<div class="btn btn-green" style="left:844px;top:28px;width:119px;height:50px;gap:8px">
  <svg width="14" height="14" viewBox="0 0 14 14"><circle cx="7" cy="7" r="6" fill="none" stroke="#fff" stroke-width="1.5"/><circle cx="7" cy="5.5" r="2" fill="#fff"/><path d="M3.5 11a4 3 0 0 1 7 0" fill="#fff"/></svg>LOGIN</div>
<div class="btn btn-blue" style="left:969px;top:28px;width:119px;height:50px">REGISTER</div>

<section class="abs hero">
  <div class="hero-photo" role="img" aria-label="Photo of teachers working together around a table in a bright classroom"></div>
  <h1 class="hero-title">WELCOME TO THE ALPEDU!</h1>
  <p class="hero-sub">Association of teachers at the Valais orientation school</p>
  <div class="btn btn-green" style="left:519px;top:224px;width:162px;height:50px;font-size:15px">OUR CALENDAR</div>
  <div class="hero-dots"><span></span><span class="on"></span><span></span><span></span></div>
  <svg class="hero-curve" width="1200" height="140" viewBox="0 0 1200 140">
    <path d="M0 0 Q600 230 1200 0 L1200 140 L0 140 Z" fill="#fff"/>
    <path d="M0 0 Q600 230 1200 0 L1200 10 Q600 265 0 12 Z" fill="var(--blue)"/>
  </svg>
</section>

<div class="abs intro-frame"></div>
<div class="abs intro-photo" role="img" aria-label="Photo of a teacher presenting to seated colleagues"></div>
<h2 class="abs heading intro-title">Stay home now. Save lives.</h2>
<ul class="abs bullet-list">
  <li><svg width="13" height="13" viewBox="0 0 13 13"><circle cx="6.5" cy="6.5" r="6.5" fill="var(--blue)"/><path d="M4 6.5h5M7 4l2.5 2.5L7 9" stroke="#fff" stroke-width="1.6" fill="none"/></svg>At vero eos et accusamus et iusto odio dignissimos duci mus qui blanditiis praesentium volupea.</li>
  <li><svg width="13" height="13" viewBox="0 0 13 13"><circle cx="6.5" cy="6.5" r="6.5" fill="var(--blue)"/><path d="M4 6.5h5M7 4l2.5 2.5L7 9" stroke="#fff" stroke-width="1.6" fill="none"/></svg>At vero eos et accusamus et iusto odio dignissimos duci mus qui blanditiis.</li>
  <li><svg width="13" height="13" viewBox="0 0 13 13"><circle cx="6.5" cy="6.5" r="6.5" fill="var(--blue)"/><path d="M4 6.5h5M7 4l2.5 2.5L7 9" stroke="#fff" stroke-width="1.6" fill="none"/></svg>At vero eos et accusamus et iusto odio dignissimos duci mus qui blanditiis praesentium volupea.</li>
  <li><svg width="13" height="13" viewBox="0 0 13 13"><circle cx="6.5" cy="6.5" r="6.5" fill="var(--blue)"/><path d="M4 6.5h5M7 4l2.5 2.5L7 9" stroke="#fff" stroke-width="1.6" fill="none"/></svg>At vero eos et accusamus et iusto odio dignissiea.</li>
</ul>
<div class="btn btn-green" style="left:685px;top:1149px;width:214px;height:51px">DOWNLOAD DOCUMENTS</div>

<section class="abs protect"></section>
<h2 class="abs heading protect-title">How we protect ourselves</h2>
<div class="card" style="left:111px"><div class="card-icon" role="img" aria-label="Hand washing icon"></div><p class="card-text">Sed ut perspici<br>atis unde</p></div>
<div class="card" style="left:360px"><div class="card-icon" role="img" aria-label="Stay at home icon"></div><p class="card-text">Sed ut perspici<br>atis unde</p></div>
<div class="card" style="left:609px"><div class="card-icon" role="img" aria-label="Distance teaching icon"></div><p class="card-text">Sed ut perspici<br>atis unde</p></div>
<div class="card" style="left:857px"><div class="card-icon" role="img" aria-label="Health care icon"></div><p class="card-text">Sed ut perspici<br>atis unde</p></div>

<svg class="abs blog-bg" width="1200" height="585" viewBox="0 0 1200 585">
  <path d="M0 112 Q600 -105 1200 112 L1200 471 Q600 690 0 471 Z" fill="var(--green-light)"/>
</svg>
<h2 class="abs heading blog-title">Latest blog</h2>
<article class="post" style="left:111px">
  <h3 class="post-title">KICK-OFF FOR OUR FUTURE HOMEPAGE</h3>
  <p class="post-date"><svg width="14" height="14" viewBox="0 0 14 14"><circle cx="7" cy="7" r="6" fill="none" stroke="var(--blue)" stroke-width="1.5"/><circle cx="7" cy="5.5" r="2" fill="var(--blue)"/><path d="M3.5 11a4 3 0 0 1 7 0" fill="var(--blue)"/></svg>20 JAN 2022</p>
  <p class="post-text">Since we can only publish updates on our website with great difficulty and the security standards are no longer up to date, we asked several companies in Upper Valais for an offer for a modern website.</p>
  <div class="btn btn-green">TEXT ONLY</div>
  <div class="follow">Follow Us: <i></i><i></i><i></i></div>
</article>
<article class="post" style="left:611px">
  <h3 class="post-title">PLEASE DO NOT RETURN ANY MORE TALONS</h3>
  <p class="post-date"><svg width="14" height="14" viewBox="0 0 14 14"><circle cx="7" cy="7" r="6" fill="none" stroke="var(--blue)" stroke-width="1.5"/><circle cx="7" cy="5.5" r="2" fill="var(--blue)"/><path d="M3.5 11a4 3 0 0 1 7 0" fill="var(--blue)"/></svg>06 DEC 2021</p>
  <p class="post-text">The registration period has expired. The vouchers should reach our members before the Christmas holidays. We sincerely wish you a peaceful Christmas time.</p>
  <div class="btn btn-green">TEXT ONLY</div>
  <div class="follow">Follow Us: <i></i><i></i><i></i></div>
</article>

<h2 class="abs heading contact-title">Contact us</h2>
<div class="field" style="left:208px;top:2454px;width:387px;height:51px">First Name</div>
<div class="field" style="left:606px;top:2454px;width:386px;height:51px">Last Name</div>
<div class="field" style="left:208px;top:2520px;width:387px;height:51px">Your Phone</div>
<div class="field" style="left:606px;top:2520px;width:386px;height:51px">Your Email</div>
<div class="field area" style="left:208px;top:2587px;width:784px;height:113px">Message</div>
<div class="btn btn-green" style="left:514px;top:2717px;width:171px;height:50px">SEND MESSAGE</div>

<svg class="abs footer-curve" width="1200" height="140" viewBox="0 0 1200 140">
  <path d="M0 133 Q600 -110 1200 133 L1200 140 L0 140 Z" fill="var(--black)"/>
  <path d="M0 133 Q600 -110 1200 133 L1200 122 Q600 -128 0 122 Z" fill="var(--blue)"/>
</svg>
<footer class="abs footer">
  <h4 class="foot-head" style="left:111px">Join our newsletter</h4>
  <div class="newsletter"><span>Email Address</span><span class="join">JOIN NOW</span></div>
  <div class="socials" aria-label="Social media links"><i></i><i></i><i></i></div>

  <h4 class="foot-head" style="left:482px">Quick links</h4>
  <ul class="foot-list" style="left:482px;top:71px">
    <li><svg width="13" height="13" viewBox="0 0 13 13"><circle cx="6.5" cy="6.5" r="6.5" fill="var(--green)"/><path d="M5 3.8l2.8 2.7L5 9.2" stroke="#000" stroke-width="1.6" fill="none"/></svg>Home</li>
    <li><svg width="13" height="13" viewBox="0 0 13 13"><circle cx="6.5" cy="6.5" r="6.5" fill="var(--green)"/><path d="M5 3.8l2.8 2.7L5 9.2" stroke="#000" stroke-width="1.6" fill="none"/></svg>Statutes Protocols</li>
    <li><svg width="13" height="13" viewBox="0 0 13 13"><circle cx="6.5" cy="6.5" r="6.5" fill="var(--green)"/><path d="M5 3.8l2.8 2.7L5 9.2" stroke="#000" stroke-width="1.6" fill="none"/></svg>Board</li>
    <li><svg width="13" height="13" viewBox="0 0 13 13"><circle cx="6.5" cy="6.5" r="6.5" fill="var(--green)"/><path d="M5 3.8l2.8 2.7L5 9.2" stroke="#000" stroke-width="1.6" fill="none"/></svg>Delegates</li>
    <li><svg width="13" height="13" viewBox="0 0 13 13"><circle cx="6.5" cy="6.5" r="6.5" fill="var(--green)"/><path d="M5 3.8l2.8 2.7L5 9.2" stroke="#000" stroke-width="1.6" fill="none"/></svg>Contact</li>
  </ul>

  <h4 class="foot-head" style="left:676px">Contact info</h4>
  <ul class="foot-list" style="left:676px;top:71px;width:210px">
    <li><svg width="11" height="14" viewBox="0 0 11 14"><path d="M5.5 0A5 5 0 0 0 .5 5c0 4 5 9 5 9s5-5 5-9a5 5 0 0 0-5-5z" fill="var(--green)"/><circle cx="5.5" cy="5" r="1.8" fill="#000"/></svg>L. Brunner, Präsident<br>Switzerland, South</li>
    <li><svg width="13" height="13" viewBox="0 0 13 13"><path d="M2.5 1l2.5 2.5-1.5 1.8a7 7 0 0 0 4.2 4.2L9.5 8 12 10.5 10.5 12C5 12 1 8 1 2.5z" fill="var(--green)"/></svg>+41 27 555 01 23</li>
    <li><svg width="14" height="11" viewBox="0 0 14 11"><rect width="14" height="11" rx="1" fill="var(--green)"/><path d="M0 1l7 5 7-5" stroke="#000" stroke-width="1.3" fill="none"/></svg>info@alpedu.ch</li>
  </ul>

  <div class="foot-brand"><span>ALPEDU</span><i></i></div>
  <div class="foot-rule"></div>
  <p class="copyright">© 2022 ALPEDU | All Rights Reserved</p>
</footer>

</body>
</html>
```